Business Card: RW Office Partners - Your tidy answer finder

Business Name: RW Office Partners
Website: www.rwofficepartners.com.au
Email: marisol@rwofficepartners.com.au
Mobile: 61 487 902 346
Facebook: @rwofficepartners
Instrgram: @rwofficepartners

Brading Colours:
HEX
#986474
#ddccd3
#7a8498
#c9d8e4
#000000
#ffffff

Tag Line: Your organised problem solver

Link to DRAFT website:
https://helpdeskhub.sitebuilderx.com/rw-office-partners

About Page from the website:
My name is Marisol Bramwell, and I would love to assist you to become more productive in your day to day and achieve your business and personal goals.
My mission is to give you time, time to work on the important tasks of your business or to be able to spend more time with your family. I will take on the tasks you don’t have time for, don’t know well or simply don’t like to do.
I have an extensive background in Administration, Tender Coordination, Document Control, WHS and Quality Management working primarily in the Construction, Mining and Corporate World.
I am passionate about being organised, having order and making things in your life (and mine) easier! I love to watch something unfold and grow into something amazing! I am known for being the go-to problem solver, the organiser of all things, producing high standards of work even under pressure. I’m also a confident communicator, and I understand that you’re busy running your business.

Target Market(s)

Small to Medium Business who require assistance in their business by a virtual assistant.

Industry/Entity Type

Virtual Assistant

Contact Information for Business Card

Mobile: 61 487 902 346

Font styles to use
Sans Serif

Colors
ffffff

Requirements
Must have
• Branding Colours as outlined.
Contact Details as outlined.
Logo as provided.
Proper contact details - mobile, facebook, instragm, website.
Simple, Elegant, very clean looking.
Should not have
• Note cute with pictures.
Not too girly as still want to market to construction companies.

```html
<!DOCTYPE html>
<html lang="en">
<head>
<meta charset="utf-8">
<title>RW Office Partners – Business Card</title>
<link rel="stylesheet" href="https://fonts.googleapis.com/css2?family=Montserrat:wght@400;500;600&family=Lato:wght@400&display=swap">
<style>
  :root {
    --mauve: #986474;
    --blush: #ddccd3;
    --slate: #7a8498;
    --mist: #c9d8e4;
    --ink: #2e2b4a;
    --text: #1c1c24;
    --paper: #ffffff;
    --decor: #f5f5f5;
  }
  * { margin: 0; padding: 0; box-sizing: border-box; }
  html, body {
    width: 1015px; height: 1200px; overflow: hidden;
    background: var(--paper);
    font-family: "Montserrat", Arial, sans-serif;
  }
  .canvas { position: relative; width: 1015px; height: 1200px; }

  .card {
    position: absolute; left: 52px; width: 904px;
    background: var(--paper);
    box-shadow: 10px 10px 14px rgba(0,0,0,0.12);
  }
  .card--front { top: 37px; height: 534px; overflow: hidden; }
  .card--back  { top: 600px; height: 543px; }

  .front-decor {
    position: absolute; left: 58px; top: -12px; width: 775px; height: 528px;
    background: var(--decor); border-radius: 40px; opacity: 0.7;
  }
  .brand {
    position: absolute; left: 0; right: 0; top: 182px;
    text-align: center;
  }
  .brand-name {
    font-weight: 500; font-size: 52px; line-height: 1.05;
    color: var(--slate); letter-spacing: 0.02em;
  }
  .brand-tagline {
    margin-top: 22px;
    font-size: 15px; font-weight: 500; letter-spacing: 0.38em;
    color: var(--text);
  }

  .accent-bar {
    position: absolute; right: 0; top: -2px; width: 15px; height: 545px;
    background: var(--mauve);
  }
  .person-name {
    position: absolute; left: 34px; top: 128px;
    font-weight: 600; font-size: 78px; line-height: 72px;
    color: var(--ink); letter-spacing: 0.02em;
  }
  .person-company {
    position: absolute; left: 36px; top: 292px;
    font-family: "Lato", Arial, sans-serif;
    font-size: 21px; letter-spacing: 0.26em; color: var(--slate);
  }
  .divider {
    position: absolute; left: 34px; top: 377px; width: 307px; height: 4px;
    background: var(--ink);
  }
  .contact {
    position: absolute; left: 330px; top: 368px;
    display: grid; grid-template-columns: 100px auto; column-gap: 16px; row-gap: 4px;
    font-size: 15px; line-height: 17px;
  }
  .contact dt { text-align: right; color: var(--mauve); font-weight: 400; }
  .contact dd { color: var(--text); font-weight: 400; letter-spacing: 0.02em; }
</style>
</head>
<body>
<main class="canvas">
  <section class="card card--front">
    <div class="front-decor" role="img" aria-label="Faint line illustration of a handshake behind the brand name"></div>
    <div class="brand">
      <div class="brand-name">RW OFFICE<br>PARTNERS</div>
      <div class="brand-tagline">YOUR TIDY ANSWER FINDER</div>
    </div>
  </section>

  <section class="card card--back">
    <div class="accent-bar"></div>
    <h1 class="person-name">MARISOL<br>BRAMWELL</h1>
    <p class="person-company">RW OFFICE PARTNERS</p>
    <div class="divider"></div>
    <dl class="contact">
      <dt>WEBSITE</dt><dd>WWW.RWOFFICEPARTNERS.COM.AU</dd>
      <dt>EMAIL</dt><dd>MARISOL@RWOFFICEPARTNERS.COM.AU</dd>
      <dt>MOBILE</dt><dd>61 487 902 346</dd>
      <dt>FACEBOOK</dt><dd>@RWOFFICEPARTNERS</dd>
      <dt>INSTRGRAM</dt><dd>@RWOFFICEPARTNERS</dd>
    </dl>
  </section>
</main>
</body>
</html>
```